Design a PRODUCT TAG for backpackers and travellers equipment/accessories company

We need a Tag Design for our products. We are a new company based in the UK called 'RoamNest'. We produce travel equipment and accessories for backpackers. Our customers are young (18-30) individuals usually GAP year makers or young professionals who enjoy travelling, adventures and exploring the world. The Tag must state our name RoamNest (at the front) and Logo(at the front) and website address www.roamnest-example.uk (on the back) and communicate our company's aim of making backpackers trip hassle free where full attention is concentrated on adventure and fun.

Target Market(s)

Young individual passionate about travelling. 18-30 age. UNI students, gap year makers or young professionals

Industry/Entity Type

Travel Industry

Colors
3276b5
33a6d7
33b8a4
abd036
fbee3d
fece3e
f68d4d
0592cd
85cae6

Requirements
Must have
• The logo and on the front
• The web address at the back
• Half of the back should be black in order to fit the product label
Nice to have
• Would be nice for the design to look like something related to travel, so for example like a plain ticket, or passport, or anything else that can be related to holiday making and travelling.

```html
<!DOCTYPE html>
<html lang="en">
<head>
<meta charset="utf-8">
<title>RoamNest product tags</title>
<link rel="stylesheet" href="https://fonts.googleapis.com/css2?family=Bebas+Neue&family=Montserrat:wght@500&display=swap">
<style>
  :root {
    --backdrop: #c9cbcd;
    --tag-white: #ffffff;
    --orange: #f5821f;
    --blue: #3276b5;
    --black: #111111;
    --ink: #141414;
  }
  * { box-sizing: border-box; margin: 0; padding: 0; }
  html, body { width: 1200px; height: 1085px; overflow: hidden; }
  body { background: var(--backdrop); position: relative; font-family: "Bebas Neue", sans-serif; }

  .tag { position: absolute; width: 247px; height: 493px; background: var(--tag-white); overflow: hidden; }
  .tag::before {
    content: ""; position: absolute; top: 2px; left: 3px; right: 3px; height: 200px;
    border: 2px dashed #222; border-bottom: none;
    border-radius: 121px 121px 0 0 / 128px 128px 0 0;
  }
  .face {
    position: absolute; top: 8px; left: 0; right: 0; bottom: 0; z-index: 1; overflow: hidden;
    border-radius: 123px 123px 0 0 / 130px 130px 0 0;
    background: var(--orange);
  }
  .back .face { bottom: auto; height: 272px; border-radius: 123px 123px 0 0 / 130px 130px 0 0; }
  .face.blue { background: var(--blue); }

  .hole {
    position: absolute; z-index: 3; top: 12px; left: 50%; width: 54px; height: 54px; margin-left: -27px;
    border-radius: 50%; background: var(--tag-white); border: 2px dashed #222;
    display: flex; align-items: center; justify-content: center;
  }
  .hole::after { content: ""; width: 22px; height: 22px; border-radius: 50%; border: 2px solid #222; }

  .brand-mark {
    position: absolute; z-index: 2; top: 88px; left: 50%; width: 124px; height: 124px; margin-left: -62px;
    border-radius: 50%; border: 2px solid var(--ink);
    display: flex; align-items: center; justify-content: center;
    font-size: 30px; color: var(--ink); letter-spacing: 1px;
  }
  .title {
    position: absolute; z-index: 2; top: 208px; left: 0; right: 0; text-align: center;
    font-size: 58px; line-height: 1; color: var(--ink); letter-spacing: 0.5px;
  }
  .light .brand-mark { border-color: #fff; color: #fff; }
  .light .title { color: #fff; }

  .scene-art { position: absolute; z-index: 1; left: 0; right: 0; }
  .front .scene-art { top: 270px; bottom: 0; }
  .art-blue { background: linear-gradient(180deg, rgba(245,130,31,0) 0%, rgba(50,118,181,0.55) 55%, var(--blue) 100%); }
  .art-white { background: linear-gradient(180deg, rgba(255,255,255,0) 0%, rgba(255,255,255,0.6) 55%, #fff 100%); }
  .art-black { background: linear-gradient(180deg, rgba(17,17,17,0) 0%, rgba(17,17,17,0.55) 55%, var(--black) 100%); }

  .back .scene-art { top: 95px; height: 145px; }
  .web-band {
    position: absolute; z-index: 2; top: 240px; left: 0; right: 0; height: 40px;
    display: flex; align-items: center; justify-content: center;
    font-family: "Montserrat", sans-serif; font-weight: 500; font-size: 17px; letter-spacing: 0.2px;
  }
  .band-blue { background: var(--blue); color: #fff; }
  .band-white { background: #fff; color: var(--ink); }
  .band-black { background: var(--black); color: #fff; }
</style>
</head>
<body>

  <!-- Row 1 -->
  <article class="tag front" style="left:47px; top:25px;">
    <div class="face"></div>
    <div class="hole"></div>
    <div class="brand-mark">RoamNest</div>
    <h1 class="title">ROAMNEST</h1>
    <div class="scene-art art-blue" role="img" aria-label="Blue silhouette of the Eiffel Tower, a giraffe, a palm tree, a bird, an elephant and a flamingo"></div>
  </article>

  <article class="tag back" style="left:317px; top:25px;">
    <div class="face"></div>
    <div class="hole"></div>
    <div class="scene-art art-blue" role="img" aria-label="Blue silhouette skyline of the Eiffel Tower, palm tree, giraffe, rhino, deer and acacia trees"></div>
    <p class="web-band band-blue">www.roamnest-example.uk</p>
  </article>

  <article class="tag front" style="left:607px; top:25px;">
    <div class="face"></div>
    <div class="hole"></div>
    <div class="brand-mark">RoamNest</div>
    <h1 class="title">ROAMNEST</h1>
    <div class="scene-art art-white" role="img" aria-label="White silhouette of the Eiffel Tower, a giraffe, a palm tree, a bird, an elephant and a flamingo"></div>
  </article>

  <article class="tag back" style="left:896px; top:25px;">
    <div class="face"></div>
    <div class="hole"></div>
    <div class="scene-art art-white" role="img" aria-label="White silhouette skyline of the Eiffel Tower, palm tree, giraffe, rhino, deer and acacia trees"></div>
    <p class="web-band band-white">www.roamnest-example.uk</p>
  </article>

  <!-- Row 2 -->
  <article class="tag front" style="left:47px; top:552px;">
    <div class="face"></div>
    <div class="hole"></div>
    <div class="brand-mark">RoamNest</div>
    <h1 class="title">ROAMNEST</h1>
    <div class="scene-art art-blue" role="img" aria-label="Blue silhouette of the Eiffel Tower, a giraffe, a palm tree, a bird, an elephant and a flamingo"></div>
  </article>

  <article class="tag back" style="left:317px; top:552px;">
    <div class="face blue"></div>
    <div class="hole"></div>
    <div class="scene-art art-black" role="img" aria-label="Black silhouette skyline of the Eiffel Tower, palm tree, giraffe, rhino, deer and acacia trees"></div>
    <p class="web-band band-black">www.roamnest-example.uk</p>
  </article>

  <article class="tag front light" style="left:610px; top:552px;">
    <div class="face"></div>
    <div class="hole"></div>
    <div class="brand-mark">RoamNest</div>
    <h1 class="title">ROAMNEST</h1>
    <div class="scene-art art-black" role="img" aria-label="Black silhouette of the Eiffel Tower, a giraffe, a palm tree, a bird, an elephant and a flamingo"></div>
  </article>

  <article class="tag back" style="left:899px; top:552px;">
    <div class="face"></div>
    <div class="hole"></div>
    <div class="scene-art art-black" role="img" aria-label="Black silhouette skyline of the Eiffel Tower, palm tree, giraffe, rhino, deer and acacia trees"></div>
    <p class="web-band band-black">www.roamnest-example.uk</p>
  </article>

</body>
</html>
```